Financial planning firm needs business card designed

Hello

I am looking to have a standard size business card designed for our agents. Attached is our logo.

Industry/Entity Type

Financial Service

Requirements
Must have
• Marcus Pellow
• Mortgage Agent
• Investment Specialist
• Office Address: 7 Bramble Ave. W., Suite K300, Hamilton, ON L9K 2R6
• Office Ph#: (905) 555-0148 x 317
• email: mpellow@corvantifg.com
• www.corvantifg.com
• TLRA Lic# 40513
Nice to have
• On the back maybe put:
• 8% to 12% Fixed per year! Ask me how.

```html
<!DOCTYPE html>
<html lang="en">
<head>
<meta charset="utf-8">
<title>Corvanti Financial Group – Business Card</title>
<link rel="stylesheet" href="https://fonts.googleapis.com/css2?family=Oswald:wght@500&family=PT+Sans:wght@400;700&display=swap">
<style>
  :root {
    --ink: #322a37;
    --ink-deep: #2a2330;
    --teal: #62e0d3;
    --teal-soft: #8cebe1;
    --teal-deep: #3fb5a8;
    --paper: #f2f2f2;
    --white: #ffffff;
  }
  * { margin: 0; padding: 0; box-sizing: border-box; }
  html, body { width: 1200px; height: 1150px; overflow: hidden; }
  body {
    background: var(--paper);
    font-family: "PT Sans", Arial, sans-serif;
    display: flex;
    align-items: center;
    justify-content: center;
    gap: 40px;
  }
  .card {
    position: relative;
    width: 540px;
    height: 326px;
    background: var(--ink);
    overflow: hidden;
    box-shadow: 0 6px 18px rgba(0,0,0,.18);
  }
  .card-shapes { position: absolute; inset: 0; }

  .brand {
    position: absolute;
    display: flex;
    flex-direction: column;
    align-items: center;
    color: var(--white);
    font-family: "PT Sans", Arial, sans-serif;
    font-weight: 400;
    text-align: center;
  }
  .brand-mark { width: 58px; height: 58px; background: var(--teal); margin-bottom: 12px; }
  .brand-name { font-size: 34px; letter-spacing: 6px; line-height: 1; }
  .brand-sub { font-size: 11px; letter-spacing: 3px; margin-top: 4px; }

  .front .brand { left: 0; right: 0; top: 92px; }
  .tagline {
    position: absolute; left: 0; right: 0; top: 272px;
    text-align: center; color: var(--white); font-size: 14px;
  }

  .back .brand { left: 36px; width: 210px; top: 108px; }
  .back .brand-mark { width: 46px; height: 46px; margin-bottom: 10px; }
  .back .brand-name { font-size: 26px; letter-spacing: 4px; }
  .back .brand-sub { font-size: 9px; letter-spacing: 2px; }

  .licence {
    position: absolute; left: 40px; top: 276px;
    color: var(--teal); font-size: 12px;
  }
  .agent { position: absolute; left: 342px; top: 64px; }
  .agent-name {
    font-family: "Oswald", "Arial Narrow", sans-serif;
    font-weight: 500; font-size: 25px; line-height: 1;
    color: var(--ink); text-transform: uppercase;
  }
  .agent-role {
    font-size: 12px; color: var(--ink); text-transform: uppercase; line-height: 1.2;
  }
  .agent-title {
    position: absolute; left: 335px; right: 0; top: 114px; height: 21px;
    background: var(--ink); color: var(--white);
    font-family: "Oswald", "Arial Narrow", sans-serif; font-weight: 500;
    font-size: 15px; line-height: 21px; padding-left: 8px; text-transform: uppercase;
  }
  .contact {
    position: absolute; left: 0; top: 0; width: 100%; height: 100%;
    list-style: none; color: var(--ink); font-size: 13px;
  }
  .contact li { position: absolute; line-height: 1.25; }
  .contact .icon { position: absolute; width: 16px; height: 16px; }
</style>
</head>
<body>

<!-- Front -->
<section class="card front" aria-label="Card front">
  <svg class="card-shapes" viewBox="0 0 540 326" aria-hidden="true">
    <polygon points="0,0 332,0 322,31 0,31" fill="var(--teal)"/>
    <polygon points="228,0 332,0 322,31 218,31" fill="var(--teal-deep)"/>
    <polygon points="216,298 540,298 540,326 206,326" fill="var(--teal)"/>
    <polygon points="216,298 300,298 310,326 206,326" fill="var(--teal-deep)"/>
  </svg>
  <div class="brand">
    <span class="brand-mark"></span>
    <span class="brand-name">CORVANTI</span>
    <span class="brand-sub">FINANCIAL GROUP</span>
  </div>
  <p class="tagline">8% to 12% Fixed per year! Ask me how</p>
</section>

<!-- Back -->
<section class="card back" aria-label="Card back">
  <svg class="card-shapes" viewBox="0 0 540 326" aria-hidden="true">
    <defs>
      <linearGradient id="panel" x1="0" y1="0" x2="1" y2="1">
        <stop offset="0" stop-color="var(--teal)"/>
        <stop offset="1" stop-color="var(--teal-soft)"/>
      </linearGradient>
    </defs>
    <rect x="14" y="78" width="6" height="166" fill="var(--teal)"/>
    <polygon points="303,0 540,0 540,326 225,326" fill="url(#panel)"/>
    <polygon points="278,112 304,112 262,326 212,326 250,150" fill="var(--teal-deep)"/>
    <polygon points="304,112 316,112 274,326 262,326" fill="var(--teal)"/>
  </svg>

  <div class="brand">
    <span class="brand-mark"></span>
    <span class="brand-name">CORVANTI</span>
    <span class="brand-sub">FINANCIAL GROUP</span>
  </div>
  <p class="licence">TLRA Lic# 40513</p>

  <div class="agent">
    <h1 class="agent-name">Marcus Pellow</h1>
    <p class="agent-role">Mortgage Agent</p>
  </div>
  <p class="agent-title">Investment Specialist</p>

  <ul class="contact">
    <li style="left:335px;top:158px">(905) 555-0148 x 317</li>
    <li style="left:340px;top:190px">mpellow@corvantifg.com</li>
    <li style="left:333px;top:215px">7 Bramble Ave. W., Suite K300<br>Hamilton, ON L9K 2R6</li>
    <li style="left:328px;top:258px;font-weight:700">www.corvantifg.com</li>
  </ul>

  <svg class="card-shapes" viewBox="0 0 540 326" aria-hidden="true">
    <g fill="var(--white)" stroke="none">
      <!-- phone -->
      <path d="M297 159c2-1 3 0 4 2l1 3c0 1-1 2-2 2 1 3 3 5 6 6 0-1 1-2 2-2l3 1c2 1 2 2 1 4-2 2-5 2-9-1-4-3-7-7-6-15z"/>
      <!-- mail -->
      <rect x="289" y="191" width="17" height="11"/>
      <path d="M289 191l8.5 6 8.5-6" stroke="var(--teal-deep)" stroke-width="1.4" fill="none"/>
      <!-- home -->
      <path d="M284 223l9-8 9 8h-3v8h-4v-5h-4v5h-4v-8z"/>
      <!-- globe -->
      <circle cx="278" cy="258" r="8"/>
      <path d="M270 258h16M278 250v16M272 253h12M272 263h12" stroke="var(--teal-deep)" stroke-width="1.2" fill="none"/>
    </g>
  </svg>
</section>

</body>
</html>
```